Brindle Works PPT design

We are looking for a fresh and funky PPT design that is both eye-catching and allows room/whitespace for us to get the content across. We are a social media agency based in China and our logo although simple sort of reflects the nature of the company. There are two main tasks for this PPT, one as a business card to show-case our case-studies, but also as a back-drop to our pitch presentations and other client presentations. These presentations are a mix of visuals, text and graphs. The key message we want to get across is that we are professional, creative and fresh. We think that using our four support colours may work but are open to suggestions.
Current website www.brindleworks-demo.com
Reason: Hi All,
as we have just guaranteed the payment we extended the deadline to allow for more submissions. Please bear with us.
Thanks,
Brindle Works Team
Reason: To see more designs, we extend the deadline to March 18, 2014. Thanks.
Target Market(s)
Marketing CMO's, company CEO's, product managers, social media managers
Industry/Entity Type
Business
Look and feel

```html
<!DOCTYPE html>
<html lang="en">
<head>
<meta charset="utf-8">
<title>Brindle Works – Who We Are</title>
<link rel="stylesheet" href="https://fonts.googleapis.com/css2?family=Saira:wght@400;600;700&family=Roboto+Slab:wght@300;400&display=swap">
<style>
  :root {
    --page-bg: #d9d7d2;
    --slide-bg: #ffffff;
    --ink: #111319;
    --orange: #e55a22;
    --green: #7dc527;
    --magenta: #e2007a;
    --purple: #6c0f7a;
    --olive-text: #5d6b4c;
    --body-grey: #9a9a9a;
    --heading-grey: #333333;
    --icon-purple: #9b4fb3;
    --divider: #cfcfcf;
  }
  * { margin: 0; padding: 0; box-sizing: border-box; }
  html, body {
    width: 1200px; height: 1000px; overflow: hidden;
    background: var(--page-bg);
  }
  .slide {
    position: absolute; left: 30px; top: 72px;
    width: 1024px; height: 768px;
    background: var(--slide-bg);
    transform: scale(1.113); transform-origin: top left;
    box-shadow: 0 4px 14px rgba(0,0,0,.25);
    overflow: hidden;
  }
  .slide-title {
    position: absolute; top: 10px; left: 0; width: 100%;
    text-align: center;
    font: 700 48px/56px "Saira", sans-serif;
    letter-spacing: 1px; color: var(--ink);
  }
  .colour-band {
    position: absolute; top: 78px; left: 0; width: 100%; height: 26px;
    display: flex;
  }
  .colour-band span { flex: 1; }
  .band-orange { background: var(--orange); }
  .band-green { background: var(--green); }
  .band-magenta { background: var(--magenta); }
  .band-purple { background: var(--purple); }
  .tagline {
    position: absolute; top: 154px; left: 0; width: 100%;
    text-align: center;
    font: 600 29px/36px "Saira", sans-serif;
    color: var(--green); letter-spacing: .5px;
  }
  .intro {
    position: absolute; top: 216px; left: 36px; width: 960px;
    font: 400 22px/31px "Saira", sans-serif;
    color: var(--olive-text); text-indent: 38px;
  }
  .feature {
    position: absolute; top: 338px; width: 446px;
    text-align: center;
  }
  .feature-team { left: 28px; }
  .feature-industries { left: 548px; }
  .feature-icon { display: block; margin: 0 auto; }
  .feature-heading {
    margin-top: 20px;
    font: 400 18px/24px "Roboto Slab", serif;
    color: var(--heading-grey);
  }
  .feature-text {
    margin-top: 10px;
    font: 300 12.3px/21px "Roboto Slab", serif;
    color: var(--body-grey);
  }
  .feature-divider {
    position: absolute; left: 511px; top: 414px;
    width: 2px; height: 175px; background: var(--divider);
  }
  .footer-bar {
    position: absolute; left: 0; top: 708px; width: 100%; height: 18px;
    background: var(--ink);
  }
  .brand {
    position: absolute; left: 72px; top: 694px;
    height: 46px; padding: 0 20px;
    background: var(--slide-bg); border-radius: 23px;
    display: flex; align-items: center; gap: 8px;
  }
  .brand-mark { width: 10px; height: 10px; background: var(--purple); }
  .brand-name {
    font: 700 24px/1 "Saira", sans-serif; color: var(--ink);
    letter-spacing: -.3px;
  }
  .page-number {
    position: absolute; left: 934px; top: 680px;
    width: 76px; height: 72px; border-radius: 14px;
    background: var(--ink); padding: 9px;
  }
  .page-number span {
    display: flex; align-items: center; justify-content: center;
    width: 100%; height: 100%; border-radius: 9px;
    background: var(--green);
    font: 700 30px/1 "Saira", sans-serif; color: var(--ink);
  }
</style>
</head>
<body>
<main class="slide">
  <h1 class="slide-title">WHO WE ARE</h1>
  <div class="colour-band">
    <span class="band-orange"></span><span class="band-green"></span><span class="band-magenta"></span><span class="band-purple"></span>
  </div>

  <h2 class="tagline">Forever learning, forever pushing</h2>
  <p class="intro">We don't sit back on our laurels, we consistently push to learn and reapply ourselves to truly be able to add value to our clients' business</p>

  <section class="feature feature-team">
    <svg class="feature-icon" width="56" height="56" viewBox="0 0 56 56" aria-hidden="true">
      <circle cx="28" cy="28" r="26" fill="none" stroke="var(--icon-purple)" stroke-width="2"/>
      <circle cx="23" cy="22" r="5" fill="var(--icon-purple)"/>
      <path d="M14 38c0-7 4-10 9-10s9 3 9 10z" fill="var(--icon-purple)"/>
      <circle cx="33" cy="21" r="4.5" fill="var(--icon-purple)"/>
      <path d="M30 27c1-.6 2-.8 3-.8 5 0 9 3 9 11.8h-8c0-5-1.5-8.5-4-11z" fill="var(--icon-purple)"/>
    </svg>
    <h3 class="feature-heading">Team</h3>
    <p class="feature-text">The Brindle Works team are a group of dedicated professionals with varying areas of expertise. We believe we have found a great balance of strategists, project managers and content creators that can tackle most industries. We have proven adept at acquiring the right knowledge to be able to get into the nitty-gritty of each industry we work for and deliver truly outstanding work that is both relevant and interactive. All with a great team-spirit and a can-do attitude.</p>
  </section>

  <div class="feature-divider"></div>

  <section class="feature feature-industries">
    <svg class="feature-icon" width="56" height="56" viewBox="0 0 56 56" aria-hidden="true">
      <circle cx="28" cy="28" r="26" fill="none" stroke="var(--icon-purple)" stroke-width="2"/>
      <path d="M23 19h10v4h-2v-2h-6v2h-2z" fill="var(--icon-purple)"/>
      <rect x="15" y="22" width="26" height="17" rx="2" fill="var(--icon-purple)"/>
      <rect x="15" y="29" width="26" height="1.5" fill="#ffffff"/>
      <rect x="26.5" y="27.5" width="3" height="4.5" fill="#ffffff"/>
    </svg>
    <h3 class="feature-heading">Industries</h3>
    <p class="feature-text">We have experience across many different industries and do not specialize in a sector as we believe that keeps both the thinking fresh and invigorates the team to constantly learn from each new category that we operate in. The however does not stop us from leveraging on our experience across luxury, fashion-retail, automotive, travel &amp; tourism, research, media, technology, food and wine and FMCG brands. To find out which clients we have experience with click below:</p>
  </section>

  <div class="footer-bar"></div>
  <div class="brand">
    <span class="brand-mark"></span>
    <span class="brand-name">Brindle Works</span>
  </div>
  <div class="page-number"><span>01</span></div>
</main>
</body>
</html>
```